Healthcare Service Provider looking for PowerPoint Template

ROV Profile of the company & business activity
===================================
ROV is the leading after-sale healthcare services provider in Kuwait. The IT department in the company sells & executes Healthcare IT projects in hospitals that mainly cover:

1. IT Infrastructure covering data center, disaster recovery, servers, virtualization, backup, redundancy & high-availability, multi-site connectivity, wired & wireless networking, OS & network management, software subscriptions, …etc.

2. Healthcare IT systems covering the Hospital Management system, Electronic Medical Record, evidence-based clinical content, clinical decision support systems, Radiology information system, Lab information system, pharmacy management system, ICU system, dental system, dietary & nutrition system, integration with 3rd party systems in the hospital

3. Human resources covering the company specialized teams of clinical informatics specialists, pharmacists, nurses, project managers, user experience specialists, integration specialists, systems analysts, systems developers, DB administrators, Network administrators, system architects, systems engineers, …

The assortment of these professionals handle the services for implementing specialty Healthcare IT systems, training hospital staff & healthcare professionals, on-site support & maintenance of implemented healthcare systems at the hospital

Requested design job
================
We require a PowerPoint template to be used by the IT department in presenting sales & marketing pitches, commercial proposals, projects, and related to the business activities described in the profile.

The design of the PowerPoint template should:

. be personalized for the business activities of the IT department. promote the corporate brand identity of the company. provide clean, modern and fluent look & feel for presenting on screen, projector or printing. include font selection & design as part of the template design. light colored background

. multiple page layouts & slide types like a cover slide, title slide, different types of content slides, ….

. include design collaterals like icons and clip-arts

. have common design elements in PowerPoint Master slides

Included are the current corporate logos of the company.

In summary, simplicity, fluency and personality are key to the design we seek.

Requirements
Must have
• The design of the PowerPoint template should:
• . be personalized for the business activities of the IT department. promote the corporate brand identity of the company. provide clean, modern and fluent look & feel for presenting on screen, projector or printing. include font selection & design as part of the template design. light colored background
• . multiple page layouts & slide types like a cover slide, title slide, different types of content slides, ….
• . include design collaterals like icons and clip-arts
• . have common design elements in PowerPoint Master slides

```html
<!DOCTYPE html>
<html lang="en">
<head>
<meta charset="utf-8">
<title>ROV Healthcare IT – Presentation Template</title>
<link href="https://fonts.googleapis.com/css2?family=Exo+2:wght@300;400;700&family=Open+Sans:wght@400;600;700&display=swap" rel="stylesheet">
<style>
:root{
  --canvas:#e9eaec;
  --slide:#ffffff;
  --navy:#16263d;
  --muted:#9aa0a8;
  --body:#8b9199;
  --rule:#c9ced4;
  --footer:#f1f2f4;
  --slate:#5f7782;
  --slate-dark:#4b616b;
  --paper:#eceef0;
  --silver:#cfd3d6;
  --pill:#c4c8cd;
}
*{margin:0;padding:0;box-sizing:border-box}
html,body{width:1200px;height:1200px;overflow:hidden;background:var(--canvas)}
body{position:relative;font-family:"Open Sans",sans-serif}
.slide{position:absolute;width:434px;height:262px;background:var(--slide);overflow:hidden;box-shadow:0 2px 6px rgba(0,0,0,.06)}
.slide > *{position:absolute}
.col-a{left:150px}.col-b{left:616px}
.row-1{top:29px}.row-2{top:322px}.row-3{top:616px}.row-4{top:910px}

.accent-rule{width:1px;background:var(--rule);top:0}
.title-block{border-left:2px solid var(--navy);padding-left:9px;font-family:"Exo 2",sans-serif;line-height:13px;font-weight:400}
.title-block .lead{display:block;font-weight:300;font-size:13px;color:var(--muted)}
.title-block .main{display:block;font-weight:700;font-size:13px;color:var(--navy)}
.copy{font-size:4.8px;line-height:10.9px;color:var(--body)}

/* photo placeholders: soft gradients in the scene's main tones */
.photo-desk{background:
  radial-gradient(ellipse 26% 46% at 22% 42%, rgba(238,240,242,.9), rgba(238,240,242,0) 72%),
  radial-gradient(ellipse 30% 42% at 70% 38%, rgba(210,214,217,.85), rgba(210,214,217,0) 72%),
  radial-gradient(ellipse 20% 18% at 35% 92%, rgba(120,84,70,.35), rgba(120,84,70,0) 75%),
  linear-gradient(135deg,var(--slate) 0%,var(--slate-dark) 100%)}
.photo-clinic{background:
  radial-gradient(ellipse 22% 48% at 46% 58%, rgba(232,234,236,.9), rgba(232,234,236,0) 72%),
  radial-gradient(ellipse 18% 14% at 37% 12%, rgba(215,220,224,.8), rgba(215,220,224,0) 75%),
  radial-gradient(ellipse 14% 30% at 86% 45%, rgba(30,36,42,.45), rgba(30,36,42,0) 75%),
  linear-gradient(135deg,#5c747e 0%,#4d636d 100%)}
.feature-wash{left:0;top:66px;width:434px;height:156px;background:
  radial-gradient(ellipse 20% 50% at 50% 40%, rgba(228,231,234,.9), rgba(228,231,234,0) 75%),
  radial-gradient(ellipse 18% 40% at 85% 30%, rgba(222,226,229,.8), rgba(222,226,229,0) 75%),
  linear-gradient(180deg,#f0f2f4,#f8f9fa)}

.footer{left:0;bottom:0;width:434px;height:19px;background:var(--footer);display:flex;align-items:center;padding:0 22px}
.brand{display:flex;align-items:center;gap:4px;font-family:"Exo 2",sans-serif;font-weight:700;font-size:8px;color:var(--navy)}
.brand small{font-family:"Open Sans",sans-serif;font-weight:400;font-size:3.4px;color:var(--navy);width:48px;line-height:4px}
.partner{display:flex;align-items:center;gap:3px;margin-left:14px;font-family:"Exo 2",sans-serif;font-weight:700;font-size:6.5px;color:var(--navy)}
.partner i{width:9px;height:9px;border-radius:50%;background:var(--navy);display:block}
.page-num{margin-left:auto;width:16px;height:7px;border-radius:4px;background:var(--pill);color:#fff;font-size:4.5px;font-weight:700;text-align:center;line-height:7px}

.feature{top:112px;width:90px;text-align:center}
.feature svg{display:block;margin:0 auto 5px}
.feature h3{font-size:5.2px;font-weight:700;letter-spacing:.4px;color:var(--navy);margin-bottom:3px}
.feature p{font-size:4.4px;line-height:9.6px;color:var(--body);width:72px;margin:0 auto}
.feature-divider{top:127px;width:1px;height:42px;background:var(--rule)}

.card{background:#fff;box-shadow:0 2px 8px rgba(0,0,0,.08);padding:12px 19px}
.panel{background:#f7f8f9}
.subhead{font-size:6.8px;font-weight:400;color:var(--navy)}

.play{width:48px;height:48px;border-radius:50%;background:#fff;display:flex;align-items:center;justify-content:center}

.partner-grid{background:#f4f5f6;border:1px solid #e1e3e6;display:grid}
.partner-grid span{display:flex;align-items:center;justify-content:center;gap:3px;font-family:"Exo 2",sans-serif;font-weight:700;font-size:8px;color:var(--navy);border-color:#d9dce0;border-style:solid;border-width:0}
.partner-grid span i{width:7px;height:7px;border-radius:50%;background:var(--navy);display:block}
</style>
</head>
<body>

<!-- 1. Features -->
<section class="slide col-a row-1">
  <div class="accent-rule" style="left:20px;height:45px"></div>
  <div class="feature-wash" role="img" aria-label="Faint background photo of a medical desk with clipboard, drip bag and stethoscope"></div>
  <h2 class="title-block" style="left:20px;top:19px"><span class="lead">Place for the</span><span class="main">Slide Title</span></h2>
  <div class="feature" style="left:46px">
    <svg width="12" height="12" viewBox="0 0 24 24" fill="none" stroke="#16263d" stroke-width="2"><path d="M7 11v10H3V11h4zm0 0l4-8a2 2 0 013 2l-1 5h6a2 2 0 012 2l-2 7a2 2 0 01-2 2H7"/></svg>
    <h3>YOUR TITLE</h3><p>Quisque bibendum, massa sed venenatis malesuada, diam ipsum blandit urna, vel ultricies pede nulla vitae</p>
  </div>
  <div class="feature-divider" style="left:140px"></div>
  <div class="feature" style="left:139px">
    <svg width="12" height="12" viewBox="0 0 24 24" fill="none" stroke="#16263d" stroke-width="2"><rect x="2" y="4" width="20" height="13"/><path d="M8 21h8M12 17v4"/></svg>
    <h3>YOUR TITLE</h3><p>Quisque bibendum, massa sed venenatis malesuada, diam ipsum blandit urna, vel ultricies pede nulla vitae</p>
  </div>
  <div class="feature-divider" style="left:232px"></div>
  <div class="feature" style="left:230px">
    <svg width="12" height="12" viewBox="0 0 24 24"><path fill="#16263d" d="M3 3h9l9 9-9 9-9-9z"/><circle cx="8" cy="8" r="2" fill="#fff"/></svg>
    <h3>YOUR TITLE</h3><p>Quisque bibendum, massa sed venenatis malesuada, diam ipsum blandit urna, vel ultricies pede nulla vitae</p>
  </div>
  <div class="feature-divider" style="left:324px"></div>
  <div class="feature" style="left:322px">
    <svg width="12" height="12" viewBox="0 0 24 24" fill="none" stroke="#16263d" stroke-width="2"><path d="M12 2l3 7 7 .6-5.3 4.7 1.6 7.2L12 17.8 5.7 21.5l1.6-7.2L2 9.6 9 9z"/></svg>
    <h3>YOUR TITLE</h3><p>Quisque bibendum, massa sed venenatis malesuada, diam ipsum blandit urna, vel ultricies pede nulla vitae</p>
  </div>
  <footer class="footer"><div class="brand">ROV<small>Rova Health Systems</small></div><div class="partner"><i></i>PARTNER LOGO</div><span class="page-num">01</span></footer>
</section>

<!-- 2. Photo with text card -->
<section class="slide col-b row-1">
  <div class="photo-desk" style="left:0;top:0;width:363px;height:242px" role="img" aria-label="Top-down photo of hands holding a daily report clipboard beside an open laptop"></div>
  <div class="card copy" style="left:256px;top:29px;width:144px;height:184px">Donec posuere tempus massa. Duis vulputate mauris sit amet purus. Duis vestibulum. Fusce ac erat. Curabitur sagittis. Pellentesque ultricies, ante id lobortis feugiat, ipsum magna congue risus, pulvinar euismod arcu nunc ac turpis. Cum sociis natoque penatibus et magnis dis parturient montes, nascetur ridiculus mus. Aliquam vel quam ut tellus gravida faucibus. Vivamus justo est, elementum vitae, malesuada eu, fermentum in, sapien. Donec sit amet justo. In velit. Vivamus turpis pede, dignissim sed, scelerisque nec, pretium sit</div>
  <footer class="footer"><div class="brand">ROV<small>Rova Health Systems</small></div><div class="partner"><i></i>PARTNER LOGO</div><span class="page-num">01</span></footer>
</section>

<!-- 3. Text + photo split -->
<section class="slide col-a row-2">
  <div class="accent-rule" style="left:21px;height:116px"></div>
  <h2 class="title-block" style="left:21px;top:54px;padding-left:12px"><span class="lead">Place for the</span><span class="main">Slide Title</span></h2>
  <p class="copy" style="left:34px;top:98px;width:158px">Donec posuere tempus massa. Duis vulputate mauris sit amet purus. Duis vestibulum. Fusce ac erat. Curabitur sagittis. Pellentesque ultricies, ante id lobortis feugiat, ipsum magna congue risus, pulvinar euismod arcu nunc ac turpis. Cum sociis natoque penatibus et magnis dis parturient montes, nascetur ridiculus mus. Aliquam vel quam ut tellus gravida faucibus. Vivamus justo est, elementum vitae, malesuada eu, fermentum in, sapien. Donec sit amet justo. In velit. Vivamus turpis pede, dignissim sed, scelerisque nec, pretium sit amet, dui. Nam nec felis non turpis hendrerit varius. In ultricies ornare lorem.</p>
  <div class="photo-desk" style="left:238px;top:0;width:196px;height:130px" role="img" aria-label="Top-down photo of a clipboard, glass of water and laptop on a desk"></div>
  <div class="panel" style="left:238px;top:130px;width:196px;height:113px"></div>
  <h3 class="subhead" style="left:256px;top:160px">Your Title Here</h3>
  <p class="copy" style="left:256px;top:172px;width:160px">Duis bibendum adipiscing nibh. Maecenas diam risus, molestie ut, porta et, malesuada eget, nisi. In fermentum leo sed turpis. Sed lacus velit, consequat in, ultricies sit amet, malesuada et, diam. Integer mauris sem, convallis ut, consequat in, sollicitudin sed, leo. Cras purus elit, hendrerit ut, egestas eget, sagittis at, nulla. Integer justo dui, faucibus dictum, convallis sodales.</p>
  <footer class="footer"><div class="brand">ROV<small>Rova Health Systems</small></div><div class="partner"><i></i>PARTNER LOGO</div><span class="page-num">01</span></footer>
</section>

<!-- 4. Video -->
<section class="slide col-b row-2">
  <div class="accent-rule" style="left:21px;height:116px"></div>
  <h2 class="title-block" style="left:21px;top:54px;padding-left:12px"><span class="lead">Place for the</span><span class="main">Slide Title</span></h2>
  <div class="photo-desk" style="left:134px;top:66px;width:300px;height:164px" role="img" aria-label="Video still of a hand writing on a clipboard report next to a laptop"></div>
  <div class="play" style="left:265px;top:126px"><svg width="10" height="12" viewBox="0 0 10 12"><path d="M1 0l8 6-8 6z" fill="#16263d"/></svg></div>
  <footer class="footer"><div class="brand">ROV<small>Rova Health Systems</small></div><div class="partner"><i></i>PARTNER LOGO</div><span class="page-num">01</span></footer>
</section>

<!-- 5. Partner grid wide -->
<section class="slide col-a row-3">
  <div class="accent-rule" style="left:22px;height:160px"></div>
  <h2 class="title-block" style="left:22px;top:86px;padding-left:12px"><span class="lead">Place for the</span><span class="main">Slide Title</span></h2>
  <p class="copy" style="left:34px;top:116px;width:120px">Donec posuere tempus massa. Duis vulputate mauris sit amet purus. Duis vestibulum. Fusce ac erat. Curabitur sagittis. Pellentesque ultricies, ante id lobortis feugiat, ipsum magna congue risus, pulvinar euismod arcu nunc ac turpis. Cum sociis natoque penatibus et magnis dis parturient montes, nascetur</p>
  <div class="partner-grid" style="left:189px;top:54px;width:225px;height:153px;grid-template-columns:repeat(3,1fr);grid-template-rows:repeat(2,1fr);padding:10px 16px">
    <span style="border-width:0 1px 1px 0"><i></i>Nova</span>
    <span style="border-width:0 1px 1px 0"><i></i>Helix</span>
    <span style="border-width:0 0 1px 0"><i></i>Aerix</span>
    <span style="border-width:0 1px 0 0"><i></i>Orbi</span>
    <span style="border-width:0 1px 0 0"><i></i>Unity</span>
    <span><i></i>Seedo</span>
  </div>
  <footer class="footer"><div class="brand">ROV<small>Rova Health Systems</small></div><div class="partner"><i></i>PARTNER LOGO</div><span class="page-num">01</span></footer>
</section>

<!-- 6. Partner grid tall -->
<section class="slide col-b row-3">
  <div class="partner-grid" style="left:26px;top:28px;width:148px;height:199px;grid-template-columns:repeat(2,1fr);grid-template-rows:repeat(3,1fr);padding:20px 16px">
    <span style="border-width:0 1px 1px 0"><i></i>Nova</span>
    <span style="border-width:0 0 1px 0"><i></i>Helix</span>
    <span style="border-width:0 1px 1px 0"><i></i>Orbi</span>
    <span style="border-width:0 0 1px 0"><i></i>Unity</span>
    <span style="border-width:0 1px 0 0"><i></i>Seedo</span>
    <span><i></i>Aerix</span>
  </div>
  <div class="accent-rule" style="left:207px;height:130px"></div>
  <h2 class="title-block" style="left:207px;top:68px;padding-left:12px"><span class="lead">Place for the</span><span class="main">Slide Title</span></h2>
  <p class="copy" style="left:219px;top:102px;width:184px">Donec posuere tempus massa. Duis vulputate mauris sit amet purus. Duis vestibulum. Fusce ac erat. Curabitur sagittis. Pellentesque ultricies, ante id lobortis feugiat, ipsum magna congue risus, pulvinar euismod arcu nunc ac turpis. Cum sociis natoque penatibus et magnis dis parturient montes, nascetur ridiculus mus. Aliquam vel quam ut tellus gravida faucibus. Vivamus justo est, elementum vitae, malesuada eu, fermentum in, sapien. Donec sit amet justo. In velit. Vivamus turpis pede, dignissim sed, scelerisque nec, pretium sit amet, dui. Nam nec felis non turpis hendrerit varius. In ultricies ornare lorem. Quisque bibendum, massa sed venenatis malesuada, diam ipsum blandit urna, vel ultricies pede nulla vitae lacus.</p>
  <footer class="footer"><div class="brand">ROV<small>Rova Health Systems</small></div><div class="partner"><i></i>PARTNER LOGO</div><span class="page-num">01</span></footer>
</section>

<!-- 7. Diagonal photo -->
<section class="slide col-a row-4">
  <svg style="left:0;top:0" width="243" height="243" viewBox="0 0 243 243" role="img" aria-label="Diagonal crop of a photo showing a hand writing on a daily report clipboard with glasses, syringe tray and phone">
    <defs>
      <linearGradient id="diag-base" x1="0" y1="0" x2="1" y2="1"><stop offset="0" stop-color="#5f7782"/><stop offset="1" stop-color="#4b616b"/></linearGradient>
      <radialGradient id="diag-paper" cx="0.28" cy="0.68" r="0.35"><stop offset="0" stop-color="#eceef0" stop-opacity=".9"/><stop offset="1" stop-color="#eceef0" stop-opacity="0"/></radialGradient>
    </defs>
    <polygon points="0,0 242,243 0,243" fill="url(#diag-base)"/>
    <polygon points="0,0 242,243 0,243" fill="url(#diag-paper)"/>
  </svg>
  <div class="accent-rule" style="left:175px;height:77px"></div>
  <h2 class="title-block" style="left:174px;top:57px;padding-left:12px"><span class="lead">Place for the</span><span class="main">Slide Title</span></h2>
  <p class="copy" style="left:186px;top:86px;width:210px">Donec posuere tempus massa. Duis vulputate mauris sit amet purus. Duis vestibulum. Fusce ac erat. Curabitur sagittis. Pellentesque ultricies, ante id lobortis feugiat, ipsum magna congue risus, pulvinar euismod arcu nunc ac turpis. Cum sociis natoque penatibus et magnis dis parturient montes, nascetur ridiculus mus. Aliquam vel quam ut tellus gravida faucibus. Vivamus justo est, elementum vitae, malesuada eu, fermentum in, sapien. Donec sit amet justo. In velit. Vivamus turpis pede, dignissim sed, scelerisque nec, pretium sit amet, dui. Nam nec felis non turpis hendrerit varius. In ultricies ornare lorem. Quisque bibendum, massa sed venenatis malesuada, diam ipsum blandit urna, vel ultricies pede nulla vitae lacus.</p>
  <footer class="footer"><div class="brand">ROV<small>Rova Health Systems</small></div><div class="partner"><i></i>PARTNER LOGO</div><span class="page-num">01</span></footer>
</section>

<!-- 8. Full video -->
<section class="slide col-b row-4">
  <div class="photo-clinic" style="left:56px;top:35px;width:321px;height:180px" role="img" aria-label="Video still of a medical desk with clipboard, syringe tray, drip bag, stethoscope and phone"></div>
  <div class="play" style="left:193px;top:101px"><svg width="10" height="12" viewBox="0 0 10 12"><path d="M1 0l8 6-8 6z" fill="#16263d"/></svg></div>
  <footer class="footer"><div class="brand">ROV<small>Rova Health Systems</small></div><div class="partner"><i></i>PARTNER LOGO</div><span class="page-num">01</span></footer>
</section>

</body>
</html>
```